Healing Arts Brochure with Simple, Elegant, Zen Design ,

I need to create a brochure for an upcoming event and I have to complete this project in the next few days.
I would like a tri-fold or z fold type of brochure- standard size of 8.5 x 11- both sides with text

i would like the overall design to be simple, elegant and zen .... yet not too plain :-))
I would like the fonts used to be clean and clear and ... easy to read.
I would like the background color to be white/cream or light color
Please do not use too many colors when working with the descriptions of my services or break those sections up too much ... a little is ok.
I don't want the brochure to be busy

I've uploaded the text, my photo, a photo that I will be using on my website, my logo symbol without my name and several logo symbols with my name in different font styles. I am not wed to any of the various font styles of the logo just yet.
TEXT FILE IS UPLOADED
Updates

Dear Designers, The design submissions that I'm receiving so far have not been including all 3 pages of text in the brochure. I pulled my text file to update it with the instructions that there are 3 pages of text information that need to be on the brochure. Unfortunately, I'm not able to upload the text file - seems to be a glitch on the PixelTorch website.. I called for support and they won't get back to me for a couple of hours. That will be around 11:00 am PST in the USA. PLEASE CHECK BACK if you haven't already downloaded the text file. Otherwise, please add the missing information and resubmit your ideas. Thank you!! RM

Target Market(s)

My services target clients in the healing arts.

Industry/Entity Type

Event

Requirements
Must have
• Please include the colors tones of my logo and the sunset photo -golds, oranges, blues
Brochure must include my photo and the sunset photo
Should not have
• Objects like teacups etc. that have nothing to do with my services - thank you kindly
I don't want any other photos or objects on the brochure other than my photo and the sun
Please don't put the tagline in quotes
Please do not make the brochure busy with too many colors in the text.

```html
<!DOCTYPE html>
<html lang="en">
<head>
<meta charset="utf-8">
<title>Rowan Mireille – Healing Arts Brochure</title>
<link rel="stylesheet" href="https://fonts.googleapis.com/css2?family=Arimo:ital,wght@0,400;0,700;1,400&display=swap">
<style>
  :root {
    --page-bg: #eeeeec;
    --paper: #ffffff;
    --orange: #f28a12;
    --orange-deep: #e8700a;
    --gold: #fbb733;
    --pale-gold: #fde3b8;
    --blue: #1b5fa8;
    --link-blue: #19a6e0;
    --ink: #2e2a26;
  }
  * { box-sizing: border-box; margin: 0; padding: 0; }
  html, body { width: 1200px; height: 1000px; overflow: hidden; }
  body {
    background: var(--page-bg);
    font-family: "Arimo", Arial, sans-serif;
    color: var(--ink);
    position: relative;
  }
  .brochure-spread {
    position: absolute;
    left: 105px; top: 120px;
    width: 990px; height: 760px;
    display: flex;
    background: var(--paper);
    box-shadow: 0 6px 24px rgba(0,0,0,.12);
  }
  .panel { width: 330px; height: 100%; position: relative; overflow: hidden; }
  .panel + .panel { border-left: 1px solid #ececec; }

  /* Left panel: portrait and quote */
  .panel-portrait {
    background: linear-gradient(90deg, var(--gold) 0 14px, var(--orange) 14px 22px, var(--gold) 22px 30px, transparent 30px),
                linear-gradient(270deg, var(--gold) 0 14px, var(--orange) 14px 22px, var(--gold) 22px 30px, transparent 30px),
                linear-gradient(180deg, #ffcf6a 0%, #f7a531 45%, #fbd08a 100%);
  }
  .portrait-photo {
    position: absolute; left: 40px; top: 22px;
    width: 250px; height: 300px;
    background: linear-gradient(160deg, #9a9a9a, #4a4a4a 60%, #2c2c2c);
  }
  .sunset-photo {
    position: absolute; left: 30px; right: 30px; top: 330px; bottom: 0;
    background: linear-gradient(180deg, rgba(255,236,200,.92), rgba(252,214,160,.92) 60%, rgba(250,196,120,.9));
  }
  .quote {
    position: absolute; left: 46px; right: 42px; top: 360px;
    font-style: italic; font-size: 19px; line-height: 1.32; color: #3a2c1e;
  }
  .quote-author {
    position: absolute; right: 44px; top: 690px;
    font-size: 18px; color: #3a2c1e;
  }

  /* Middle panel: credentials */
  .panel-credentials { text-align: center; padding: 60px 34px 0; }
  .brand-name {
    display: inline-flex; align-items: center; gap: 8px;
    font-size: 17px; letter-spacing: .12em; text-transform: uppercase;
    color: var(--blue); font-weight: 400;
  }
  .brand-dot { width: 14px; height: 14px; border-radius: 50%; background: var(--orange); }
  .credential-list { list-style: none; margin-top: 38px; }
  .credential-list li {
    color: var(--orange); font-size: 14px; line-height: 1.3; margin-bottom: 20px;
  }
  .contact { margin-top: 42px; }
  .contact p { color: var(--link-blue); font-weight: 700; font-size: 17px; line-height: 1.35; }

  /* Right panel: cover */
  .panel-cover { padding-top: 250px; text-align: center; }
  .cover-lotus {
    position: absolute; left: 0; right: 0; bottom: 0; height: 300px;
    background: linear-gradient(165deg,
      var(--blue) 0%, var(--blue) 14%,
      var(--orange-deep) 30%, var(--orange) 50%,
      var(--gold) 72%, #fff1d6 100%);
  }
</style>
</head>
<body>
  <main class="brochure-spread">
    <section class="panel panel-portrait">
      <div class="portrait-photo" role="img" aria-label="Black and white portrait photograph of the practitioner"></div>
      <div class="sunset-photo" role="img" aria-label="Soft golden sunset photograph behind the quote"></div>
      <p class="quote">"The services that I offer focus on supporting self-care, self-empowerment and self-regulation. Healing is returning home to our inherent sense of resiliency, vitality and well-being. I am honored to work with you and support you in your own unique journey home to yourself"</p>
      <p class="quote-author">Rowan Mireille CMT, SEP</p>
    </section>

    <section class="panel panel-credentials">
      <div class="brand-name"><span class="brand-dot"></span>Rowan Mireille</div>
      <ul class="credential-list">
        <li>Somatic Balance™ Practitioner, SEP</li>
        <li>Certified Level III StillPoint® Teacher</li>
        <li>Certified Sound Healing Practitioner, Pacific Institute of Integrative Arts</li>
        <li>Certified Deepflow Breathwork Facilitator</li>
      </ul>
      <div class="contact">
        <p>www.rowanmireille.com</p>
        <p>rowan@rowanmireille.com</p>
        <p>415-555-0187</p>
      </div>
    </section>

    <section class="panel panel-cover">
      <div class="brand-name"><span class="brand-dot"></span>Rowan Mireille</div>
      <div class="cover-lotus" role="img" aria-label="Large orange and blue lotus flower decoration"></div>
    </section>
  </main>
</body>
</html>
```